Business Card Design

Cake decorating business in a small town in Australia. looking for a style that is fresh with a touch of vintage/country. liking these ideas, timber backgrounds, chalkboards, bunting, flowers and cake elements (rolling pins, cupcakes, cake stands, etc.) would consider a shot saying/statement. would like the back of the card to have wording "Specialising in delectable treats for all your special occasions" - wedding cakes - birthday cakes - special occasion cakes - novelty cakes - cupcakes, cookies, slices and cake pops. maybe incorporate a cake in design on back page. attached are a few of my favourite cakes and the start of a card design I liked.

Industry/Entity Type

Business

Contact Information for Business Card

Marigold's Sugarloft Bakes 0438 056 969Find me on (Chirpwall Logo)

Requirements
Nice to have
• timber, some of my designs, chalkboard, baking utensils
Should not have
• no red font

```html
<!DOCTYPE html>
<html lang="en">
<head>
<meta charset="utf-8">
<title>Marigold's Sugarloft Bakes — Business Card</title>
<link href="https://fonts.googleapis.com/css2?family=Open+Sans:ital,wght@0,400;0,600;0,700;1,700&display=swap" rel="stylesheet">
<style>
  :root{
    --bg:#d9d9d9;
    --ink:#0b0b0b;
    --band:rgba(16,16,16,.92);
    --paper:#ffffff;
    --soft:#cfcfcf;
    --strip-top:#55504d;
    --strip-mid:#c9c4c0;
    --strip-low:#8e8884;
    --cake-light:#cdb98a;
    --cake-dark:#3a2d22;
    --chalk-a:#7b7774;
    --chalk-b:#2c2a29;
  }
  *{box-sizing:border-box;margin:0;padding:0}
  html,body{width:1200px;height:900px;overflow:hidden}
  body{background:var(--bg);font-family:"Open Sans",Arial,sans-serif;position:relative}
  .card{position:absolute;left:290px;width:620px;height:354px;overflow:hidden;box-shadow:0 4px 14px rgba(0,0,0,.18)}
  .card--back{top:70px;background:var(--ink)}
  .card--front{top:476px;background:var(--ink)}

  /* back */
  .label{position:absolute;left:50%;top:34px;width:236px;height:112px;transform:translateX(-50%)}
  .label svg{position:absolute;inset:0}
  .label__name{position:absolute;inset:0;display:flex;align-items:center;justify-content:center;text-align:center;
    font-weight:700;font-size:17px;line-height:1.15;color:var(--ink);padding:0 40px}
  .tagline{position:absolute;top:164px;width:100%;text-align:center;color:var(--paper);
    font-weight:700;font-style:italic;font-size:16px;line-height:1.2}
  .services{position:absolute;top:218px;width:100%;text-align:center;color:var(--paper);
    font-weight:600;font-size:14px;line-height:1.55}
  .services .dot{display:inline-block;width:7px;height:7px;border-radius:50%;background:var(--paper);margin:0 10px;vertical-align:2px}
  .rule{position:absolute;left:0;width:100%;height:6px;background:var(--paper)}
  .strip{position:absolute;left:0;bottom:0;width:100%;
    background:linear-gradient(180deg,var(--strip-top) 0%,var(--strip-mid) 50%,var(--strip-low) 100%)}
  .card--back .rule{top:300px}
  .card--back .strip{height:48px}

  /* front */
  .cake-photo{position:absolute;left:0;top:0;width:100%;height:294px;
    background:radial-gradient(ellipse at 45% 45%,var(--cake-light) 0%,#8c7650 45%,var(--cake-dark) 100%);filter:brightness(.6)}
  .phone{position:absolute;top:30px;width:100%;text-align:center;color:var(--paper);font-size:15px;display:flex;justify-content:center;align-items:center;gap:8px}
  .phone svg{width:13px;height:13px}
  .chalk{position:absolute;left:50%;top:70px;width:176px;height:84px;transform:translateX(-50%)}
  .chalk svg{position:absolute;inset:0}
  .chalk__name{position:absolute;inset:0;display:flex;align-items:center;justify-content:center;text-align:center;
    color:var(--paper);font-weight:600;font-size:13px;line-height:1.25;padding:0 30px}
  .band{position:absolute;left:0;top:164px;width:100%;height:130px;background:var(--band)}
  .social{position:absolute;top:232px;width:100%;display:flex;justify-content:center;align-items:center;gap:10px}
  .social__mark{width:12px;height:12px;border-radius:50%;background:var(--soft)}
  .social__text{color:var(--soft);font-size:12px;line-height:1}
  .social__name{display:block;color:var(--paper);font-weight:700;font-size:21px;margin-top:3px}
  .card--front .rule{top:294px}
  .card--front .strip{height:54px}
</style>
</head>
<body>

<section class="card card--back" aria-label="Card back">
  <div class="label">
    <svg viewBox="0 0 236 112" aria-hidden="true">
      <path d="M30 8 H206 Q206 28 228 28 V84 Q206 84 206 104 H30 Q30 84 8 84 V28 Q30 28 30 8 Z" fill="#fff" stroke="#fff" stroke-width="3"/>
      <path d="M34 14 H202 Q202 34 222 34 V78 Q202 78 202 98 H34 Q34 78 14 78 V34 Q34 34 34 14 Z" fill="none" stroke="#111" stroke-width="2"/>
    </svg>
    <div class="label__name">Marigold's Sugarloft Bakes</div>
  </div>
  <p class="tagline">Specialising in delectable treats for all<br>your special occasions</p>
  <p class="services">
    Wedding Cakes<span class="dot"></span>Birthday cakes<span class="dot"></span>Special occasion cakes<br>
    Novelty cakes<span class="dot"></span>Cupcakes<span class="dot"></span>Cookies<span class="dot"></span>Slices and Cake pops
  </p>
  <div class="rule"></div>
  <div class="strip"></div>
</section>

<section class="card card--front" aria-label="Card front">
  <div class="cake-photo" role="img" aria-label="Photograph of a decorated birthday cake with a fondant banner"></div>
  <div class="band"></div>
  <p class="phone">
    <svg viewBox="0 0 24 24" aria-hidden="true"><path fill="#fff" d="M6.6 10.8a15 15 0 0 0 6.6 6.6l2.2-2.2a1 1 0 0 1 1-.25 11.4 11.4 0 0 0 3.6.57 1 1 0 0 1 1 1V20a1 1 0 0 1-1 1A17 17 0 0 1 3 4a1 1 0 0 1 1-1h3.5a1 1 0 0 1 1 1c0 1.25.2 2.45.57 3.57a1 1 0 0 1-.25 1z"/></svg>
    0417 382 254
  </p>
  <div class="chalk">
    <svg viewBox="0 0 176 84" aria-hidden="true">
      <defs><linearGradient id="chalkFill" x1="0" y1="0" x2="0" y2="1"><stop offset="0" stop-color="#7b7774"/><stop offset="1" stop-color="#2c2a29"/></linearGradient></defs>
      <path d="M24 4 H152 Q152 20 172 20 V64 Q152 64 152 80 H24 Q24 64 4 64 V20 Q24 20 24 4 Z" fill="url(#chalkFill)" stroke="#fff" stroke-width="2.5"/>
    </svg>
    <div class="chalk__name">Marigold's Sugarloft Bakes</div>
  </div>
  <div class="social">
    <span class="social__mark" aria-hidden="true"></span>
    <span class="social__text">find us on<span class="social__name">Chirpwall</span></span>
  </div>
  <div class="rule"></div>
  <div class="strip"></div>
</section>

</body>
</html>
```